indépendant en tant que Massothérapeute et Préparateur Mental, j'ai besoin de ...

Massothérapeute et préparateur mental indépendant, je recherche une carte de visite sobre et dynamique, sans images liées au massage ou à la préparation mentale mais intégrant mon logo. Les couleurs que j'aime bien sont : Blanc, gris, anthracite, noir et jaune

carte de préférence Horizontale
neutre qui puisse toucher le deux domaines Massothérapie et préparation mentale

Requirements
Must have
• mon projet doit intégrer au recto:
LOGO
Loïc Bardemaz
078 315 26 48
info@loicbardemaz-exemple.ch
et éventuellement www.loicbardemaz-exemple.ch

et au verso les deux adresses:

Chemin des Grèvelins 7B
1400 Yverdon-les-Bains

Avenue des Mélèzes 9
1700 Fribourg

Should not have
• mon projet ne doit pas contenir d'image en liens avec le massage ni la préparation mentale.

```html
<!DOCTYPE html>
<html lang="fr">
<head>
<meta charset="utf-8">
<title>Loïc Bardemaz – Cartes de visite</title>
<link href="https://fonts.googleapis.com/css2?family=Roboto:wght@400;500;700&family=Roboto+Condensed:wght@400;700&display=swap" rel="stylesheet">
<style>
  :root {
    --page: #141414;
    --card: #2b2b2c;
    --card-edge: #333334;
    --white: #f4f4f4;
    --grey: #bdbdbd;
    --yellow: #f5b800;
  }
  * { margin: 0; padding: 0; box-sizing: border-box; }
  html, body { width: 1200px; height: 896px; overflow: hidden; background: var(--page); }
  body {
    display: flex; flex-direction: column; align-items: center; justify-content: center; gap: 48px;
    font-family: "Roboto", sans-serif; color: var(--white);
  }
  .card {
    position: relative; width: 640px; height: 366px;
    background: linear-gradient(135deg, var(--card-edge), var(--card));
    box-shadow: 0 14px 30px rgba(0,0,0,.55);
  }

  /* Verso */
  .addresses {
    position: absolute; left: 0; right: 0; top: 50%; transform: translateY(-50%);
    display: flex; flex-direction: column; align-items: center; gap: 14px;
    font-size: 19px; letter-spacing: .2px;
  }
  .address { display: flex; align-items: center; gap: 10px; }
  .address svg { width: 14px; height: 18px; flex: none; }

  /* Recto */
  .brand {
    position: absolute; left: 96px; top: 82px;
    display: flex; align-items: center; gap: 16px;
  }
  .brand-mark { width: 34px; height: 34px; background: var(--white); flex: none; }
  .brand-name { font-size: 40px; font-weight: 700; line-height: 1; color: var(--white); letter-spacing: .5px; }
  .brand-tagline { margin-top: 8px; font-size: 11px; font-weight: 500; letter-spacing: 1.4px; text-transform: uppercase; color: var(--white); }

  .holder {
    position: absolute; left: 96px; top: 228px; width: 220px; text-align: right;
    font-family: "Roboto Condensed", sans-serif;
  }
  .holder-name { font-size: 30px; font-weight: 700; text-transform: uppercase; line-height: 1.05; }
  .holder-role { font-size: 21px; font-weight: 400; margin-top: 4px; }

  .divider { position: absolute; left: 336px; top: 226px; width: 1px; height: 76px; background: var(--yellow); }

  .contacts {
    position: absolute; left: 356px; top: 226px;
    list-style: none; display: flex; flex-direction: column; gap: 8px;
    font-size: 17px; line-height: 20px;
  }
  .contacts li { display: flex; align-items: center; gap: 9px; }
  .contacts svg { width: 14px; height: 14px; flex: none; }
</style>
</head>
<body>

<section class="card card-back" aria-label="Verso de la carte">
  <div class="addresses">
    <p class="address">
      <svg viewBox="0 0 14 18"><path d="M7 0a7 7 0 0 0-7 7c0 5 7 11 7 11s7-6 7-11a7 7 0 0 0-7-7z" fill="var(--yellow)"/><circle cx="7" cy="7" r="2.6" fill="var(--card)"/></svg>
      Chemin des Grèvelins 7B, 1400 Yverdon-les-Bains
    </p>
    <p class="address">
      <svg viewBox="0 0 14 18"><path d="M7 0a7 7 0 0 0-7 7c0 5 7 11 7 11s7-6 7-11a7 7 0 0 0-7-7z" fill="var(--yellow)"/><circle cx="7" cy="7" r="2.6" fill="var(--card)"/></svg>
      Avenue des Mélèzes 9, 1700 Freiburg
    </p>
  </div>
</section>

<section class="card card-front" aria-label="Recto de la carte">
  <div class="brand">
    <span class="brand-mark"></span>
    <div>
      <p class="brand-name">Loïc Bardemaz</p>
      <p class="brand-tagline">Massothérapeute / Préparateur mental</p>
    </div>
  </div>

  <div class="holder">
    <p class="holder-name">Loïc Bardemaz</p>
    <p class="holder-role">Founder &amp; CEO</p>
  </div>

  <span class="divider"></span>

  <ul class="contacts">
    <li>
      <svg viewBox="0 0 14 14"><path d="M3 1l2.2 2.6-1.3 1.6c.9 1.9 2.3 3.3 4.2 4.2l1.6-1.3L12.3 10.3 11 12.6C6 12.6 1.4 8 1.4 3z" fill="var(--yellow)"/></svg>
      078 315 26 48
    </li>
    <li>
      <svg viewBox="0 0 14 14"><rect x="0.5" y="2.5" width="13" height="9" fill="var(--yellow)"/><path d="M0.5 2.5L7 8l6.5-5.5" fill="none" stroke="var(--card)" stroke-width="1.2"/></svg>
      info@loicbardemaz-exemple.ch
    </li>
    <li>
      <svg viewBox="0 0 14 14"><circle cx="7" cy="7" r="6.3" fill="var(--yellow)"/><g fill="none" stroke="var(--card)" stroke-width="1"><ellipse cx="7" cy="7" rx="2.6" ry="6.3"/><path d="M0.7 7h12.6M1.8 3.8h10.4M1.8 10.2h10.4"/></g></svg>
      www.loicbardemaz-exemple.ch
    </li>
  </ul>
</section>

</body>
</html>
```